Brightpath7crew needs a website

We need a website so we can post future events of our company about business motivation. The site have to include a calendar on the "Home" page that when the user cliks on the day of the event , there should open a small page with the information of the event (location,time,subject of the event...) . We need also an "About Us" page with information about our company and what we do as well as "Contact" page with our email and phone number and access to our facebook page. We would like to have a private access for users ("Restricted access") but they have to put their e-mail and password to access the special page (log in). On the 'special page' we would like to have some videos and photos that we will post on that page regularly .
Here is a website that would be an exemple of how we would like to have ours
http://summitlarkacademy.example
The needs to be responsed and with backoffice

Industry/Entity Type

Business

Number of Pages Required

3 page

Colors
9bcb3c
f37122

Requirements
Must have
• Must have a restricted access page so the user can place a user name and a secret password.

```html
<!DOCTYPE html>
<html lang="en">
<head>
<meta charset="utf-8">
<title>Brightpath7crew – Future Events</title>
<link rel="stylesheet" href="https://fonts.googleapis.com/css2?family=Lato:ital,wght@0,400;0,700;0,900;1,900&display=swap">
<style>
:root{
  --orange:#f37122;
  --green:#9bcb3c;
  --ink:#333333;
  --body:#444444;
  --grey-bg:#f4f4f4;
  --footer:#333333;
  --white:#ffffff;
  --frame:#7d8389;
}
*{box-sizing:border-box;margin:0;padding:0}
html,body{width:1200px;height:3232px;overflow:hidden}
body{font-family:'Lato',Arial,sans-serif;color:var(--body);background:var(--white);position:relative}
.section{position:absolute;left:0;width:1200px}
.abs{position:absolute}

/* top bar */
.topbar{top:0;height:37px;background:var(--orange);color:var(--white);font-size:14px;letter-spacing:1px}
.topbar .item{top:9px;display:flex;align-items:center;gap:6px}
.topbar .social{top:5px;display:flex;gap:20px;left:810px}
.topbar .social span{width:26px;height:26px;border:2px solid var(--white);border-radius:50%;display:block}
/* nav */
.nav{top:37px;height:81px;background:var(--white)}
.brand{left:183px;top:26px;font-size:22px;color:#555;font-weight:400}
.menu{top:30px;display:flex;list-style:none}
.menu li{position:absolute;white-space:nowrap;color:var(--orange);font-weight:700;font-size:16px;letter-spacing:2px}
/* hero */
.hero{top:118px;height:554px;background:radial-gradient(ellipse at 65% 30%,#b64be0 0%,#5b2fd6 35%,#2a1a8c 60%,#120c2a 100%)}
.hero-title{left:125px;top:76px;color:var(--white);font-weight:900;font-style:italic;font-size:40px}
.hero-sub{left:285px;top:128px;color:var(--white);font-size:30px}
/* what we do */
.about{top:672px;height:464px;background:var(--grey-bg)}
.heading{font-size:37px;font-weight:700;letter-spacing:1px}
.orange{color:var(--orange)}
.green{color:var(--green)}
.about p{left:125px;top:108px;width:463px;font-size:13px;line-height:16px;color:#222}
.read-more{color:var(--orange);font-size:22px;letter-spacing:2px}
.video{left:707px;top:104px;width:340px;height:228px;background:var(--orange);border:5px solid var(--frame)}
.play{width:88px;height:88px;border-radius:50%;background:var(--green);border:3px solid var(--white);position:absolute;left:50%;top:50%;transform:translate(-50%,-50%)}
.play::after{content:"";position:absolute;left:33px;top:24px;border-left:28px solid var(--white);border-top:17px solid transparent;border-bottom:17px solid transparent}
.see-video{left:912px;top:378px;font-size:13px;letter-spacing:3px;color:#222}
/* services */
.services{top:1136px;height:552px;background:var(--green)}
.services .heading{width:1200px;text-align:center;top:16px;letter-spacing:8px;font-size:38px}
.dark{color:var(--ink)}
.card{width:433px;height:185px;border:2px solid var(--orange);position:absolute}
.card h3{position:absolute;left:32px;top:8px;color:var(--orange);font-size:15px;letter-spacing:2px;font-weight:400}
.card p{position:absolute;left:12px;top:40px;width:255px;font-size:11px;line-height:17px;color:#2d3a10;letter-spacing:1px}
.card .read-more{position:absolute;left:12px;bottom:6px}
.card .thumb{position:absolute;right:10px;top:6px;width:146px;height:166px;background:linear-gradient(180deg,#f1f1f1,#d9d9d9)}
.card .play{width:44px;height:44px;border-width:2px}
.card .play::after{left:16px;top:11px;border-left-width:14px;border-top-width:9px;border-bottom-width:9px}
/* help */
.help{top:1688px;height:374px;background:var(--white)}
.portrait{left:155px;top:21px;width:196px;height:353px;background:linear-gradient(180deg,#f3f3f3 0%,#d8c6b8 40%,#3a4656 75%,#2a3340 100%)}
.help h2{left:440px;top:40px;font-size:22px;letter-spacing:1.5px;font-weight:700}
.help p{left:429px;top:88px;width:556px;font-size:13px;line-height:16px;letter-spacing:.6px;color:#222}
.tips-title{left:427px;top:216px;font-size:13px;color:var(--orange);letter-spacing:1px}
.tips{list-style:none}
.tips li{position:absolute;left:427px;display:flex;align-items:center;gap:42px;font-size:13px;letter-spacing:.6px;color:#333;white-space:nowrap}
.tips li::before{content:"";width:24px;height:24px;border:2px solid var(--orange);border-radius:50%}
.tips li.active{color:var(--green)}
/* search */
.search{top:2062px;height:179px;background:var(--green)}
.tab{top:20px;height:22px;background:var(--orange);color:var(--white);font-size:12px;letter-spacing:2px;text-align:center;line-height:22px}
.or{left:568px;top:17px;color:var(--white);font-size:18px;letter-spacing:2px}
.field-label{top:64px;color:var(--white);font-size:20px;font-weight:700;letter-spacing:1px}
.field{top:89px;height:34px;background:var(--white)}
.search-btn{left:463px;top:138px;width:183px;height:37px;background:var(--orange);border:2px solid var(--white);color:var(--white);font-size:20px;letter-spacing:2px;display:flex;align-items:center;padding-left:18px;gap:40px}
/* testimonials */
.testimonials{top:2241px;height:339px;background:var(--white)}
.testimonials h2{left:0;width:1216px;text-align:center;top:30px;font-size:36px;font-weight:900;color:#555;letter-spacing:1px}
.avatar{width:120px;height:120px;border-radius:50%;border:5px solid var(--orange);background:linear-gradient(180deg,#e8eef4,#9aa9b8)}
.t-name{font-size:28px;color:#444}
.t-role{font-size:28px;color:var(--green);border-bottom:2px solid #f6b48a;padding-bottom:2px}
.t-text{width:320px;font-size:15px;line-height:21px;color:#333}
/* schedule */
.schedule{top:2580px;left:0;width:593px;height:448px;background:var(--orange);border:2px solid #fff;border-left:none;position:absolute}
.schedule h2,.contact h2{font-size:32px;color:var(--white);font-weight:900}
.cal{left:140px;top:114px;display:grid;grid-template-columns:repeat(7,60px);row-gap:21px;color:var(--white);font-size:16px;font-weight:700;text-align:center}
.cal .head{font-size:17px}
.cal .today{color:var(--green)}
.btn{position:absolute;color:var(--white);font-size:30px;font-weight:900;text-align:center;letter-spacing:1px}
.contact{top:2580px;left:593px;width:607px;height:448px;background:var(--green);position:absolute}
.input{position:absolute;left:84px;width:370px;background:var(--white);color:#555;font-size:20px;padding:8px 0 0 28px}
/* footer */
.footer{top:3028px;height:204px;background:var(--footer);color:var(--white)}
.footer .social span{position:absolute;top:23px;width:54px;height:54px;border:2px solid var(--white);border-radius:50%}
.footer-links{top:98px;width:1200px;text-align:center;font-size:15px;letter-spacing:1px;word-spacing:4px}
.footer-links span{margin:0 20px}
.copy{top:162px;width:1200px;text-align:center;font-size:14px}
</style>
</head>
<body>

<header>
  <div class="section topbar">
    <div class="abs item" style="left:250px">
      <svg width="18" height="18" viewBox="0 0 24 24" fill="#fff"><path d="M6.6 10.8a15 15 0 0 0 6.6 6.6l2.2-2.2a1 1 0 0 1 1-.25 11.4 11.4 0 0 0 3.6.6 1 1 0 0 1 1 1V20a1 1 0 0 1-1 1A17 17 0 0 1 3 4a1 1 0 0 1 1-1h3.5a1 1 0 0 1 1 1c0 1.25.2 2.45.6 3.6a1 1 0 0 1-.25 1z"/></svg>
      <span>1234-567890</span>
    </div>
    <div class="abs item" style="left:428px">
      <svg width="18" height="14" viewBox="0 0 18 14" fill="none" stroke="#fff" stroke-width="1.6"><rect x="1" y="1" width="16" height="12"/><path d="M1 1l8 6 8-6"/></svg>
      <span>info@brightpath7crew.example</span>
    </div>
    <div class="abs social"><span></span><span></span><span></span></div>
    <div class="abs item" style="left:955px">Clint Login</div>
  </div>
  <nav class="section nav">
    <div class="abs brand">Brightpath7crew</div>
    <ul class="menu">
      <li style="left:414px">HOME</li>
      <li style="left:524px">ABOUT US</li>
      <li style="left:675px">MEETINGS</li>
      <li style="left:828px">EVENTS</li>
      <li style="left:953px">CONTACT</li>
    </ul>
  </nav>
</header>

<section class="section hero" role="img" aria-label="Audience watching a presenter on a stage lit in blue and purple">
  <h1 class="abs hero-title">Welcoem to Team Brightpath7crew</h1>
  <p class="abs hero-sub">Find our Future Events</p>
</section>

<section class="section about">
  <h2 class="abs heading" style="left:125px;top:32px"><span class="orange">WHAT</span> <span class="green">WE DO</span></h2>
  <p class="abs">Lorem ipsum dolor sit amet, consectetur adipisicing elit, sed do eiusmod tempor incididunt ut labore et dolore magna aliqua. Ut enim ad minim veniam, quis nostrud exercitation ullamco laboris nisi ut aliquip ex ea commodo consequat. Duis aute irure dolor in reprehenderit in voluptate velit esse cillum dolore eu fugiat nulla pariatur. Excepteur sint occaecat cupidatat non proident, sunt in culpa qui officia deserunt mollit anim id est laborum. Sed ut perspiciatis unde omnis iste natus error sit voluptatem accusantium doloremque laudantium, totam rem aperiam, eaque ipsa quae ab illo inventore veritatis et quasi architecto beatae vitae dicta sunt explicabo. Nemo enim ipsam voluptatem quia voluptas sit aspernatur aut odit aut fugit, sed quia consequuntur magni dolores eos qui ratione voluptatem sequi nesciunt. Neque porro quisquam est, qui dolorem ipsum quia dolor sit amet, consectetur, adipisci velit, sed quia non numquam eius modi tempora incidunt ut labore</p>
  <div class="abs read-more" style="left:125px;top:414px">Read More</div>
  <h2 class="abs heading green" style="left:707px;top:32px">VIEW OUR VIDEO</h2>
  <div class="abs video"><span class="play"></span></div>
  <svg class="abs" style="left:805px;top:335px" width="100" height="60" viewBox="0 0 100 60" fill="none" stroke="#222" stroke-width="2"><path d="M8 4 C10 30 30 46 95 50"/><path d="M2 14 L8 3 L16 12"/></svg>
  <div class="abs see-video">SEE OUR VEDIO'S</div>
</section>

<section class="section services">
  <h2 class="abs heading"><span class="dark">OUR</span> <span class="orange">SERVICES</span></h2>
  <article class="card" style="left:151px;top:90px">
    <h3>EVENT VEDIOS</h3>
    <p>Lorem ipsum dolor sit amet, consectetur adipisicing elit, sed do eiusmod tempor incididunt ut labore et dolore magna aliqua. Ut enim ad minim veniam, quis nostrud exercitation ullamco laboris nisi ut</p>
    <div class="read-more">Read More</div>
    <div class="thumb" role="img" aria-label="Smiling presenter in a dark suit gesturing to the side"><span class="play"></span></div>
  </article>
  <article class="card" style="left:616px;top:90px">
    <h3>CULTURAL VEDIOS</h3>
    <p>Lorem ipsum dolor sit amet, consectetur adipisicing elit, sed do eiusmod tempor incididunt ut labore et dolore magna aliqua. Ut enim ad minim veniam, quis nostrud exercitation ullamco laboris nisi ut</p>
    <div class="read-more">Read More</div>
    <div class="thumb" role="img" aria-label="Smiling presenter in a dark suit gesturing to the side"><span class="play"></span></div>
  </article>
  <article class="card" style="left:151px;top:323px">
    <h3>ANNUAL VEDIOS</h3>
    <p>Lorem ipsum dolor sit amet, consectetur adipisicing elit, sed do eiusmod tempor incididunt ut labore et dolore magna aliqua. Ut enim ad minim veniam, quis nostrud exercitation ullamco laboris nisi ut</p>
    <div class="read-more">Read More</div>
    <div class="thumb" role="img" aria-label="Smiling presenter in a dark suit gesturing to the side"><span class="play"></span></div>
  </article>
  <article class="card" style="left:616px;top:323px">
    <h3>MONTHLY VEDIOS</h3>
    <p>Lorem ipsum dolor sit amet, consectetur adipisicing elit, sed do eiusmod tempor incididunt ut labore et dolore magna aliqua. Ut enim ad minim veniam, quis nostrud exercitation ullamco laboris nisi ut</p>
    <div class="read-more">Read More</div>
    <div class="thumb" role="img" aria-label="Smiling presenter in a dark suit gesturing to the side"><span class="play"></span></div>
  </article>
</section>

<section class="section help">
  <div class="abs portrait" role="img" aria-label="Portrait of a smiling man in a blazer"></div>
  <h2 class="abs"><span class="orange">How Can Brightpath7crew</span> <span class="green">Help to Find an Event</span></h2>
  <p class="abs">Lorem ipsum dolor sit amet, consectetur adipisicing elit, sed do eiusmod tempor incididunt ut labore et dolore magna aliqua. Ut enim ad minim veniam, quis nostrud exercitation ullamco laboris nisi ut aliquip ex ea commodo consequat. Duis aute irure dolor in reprehenderit in voluptate velit esse cillum dolore eu fugiat nulla pariatur. Excepteur sint occaecat cupidatat non proident, sunt in culpa qui officia deserunt mollit anim id</p>
  <div class="abs tips-title">Recent Advice and Tips</div>
  <ul class="tips">
    <li style="top:255px">Lorem ipsum dolor sit amet, consectetur adipisicing</li>
    <li class="active" style="top:288px">Lorem ipsum dolor sit amet, consectetur adipisicing</li>
    <li style="top:322px">Lorem ipsum dolor sit amet, consectetur adipisicing</li>
  </ul>
</section>

<section class="section search">
  <div class="abs tab" style="left:338px;width:222px">Event Search</div>
  <div class="abs or">OR</div>
  <div class="abs tab" style="left:586px;width:181px">Recent Event</div>
  <label class="abs field-label" style="left:153px">KEYWORDS</label>
  <label class="abs field-label" style="left:427px">LOCATION</label>
  <label class="abs field-label" style="left:705px">CATEGORY</label>
  <div class="abs field" style="left:153px;width:248px"></div>
  <div class="abs field" style="left:427px;width:250px"></div>
  <div class="abs field" style="left:705px;width:250px"></div>
  <div class="abs search-btn">SEARCH
    <svg width="26" height="26" viewBox="0 0 26 26" fill="none" stroke="#fff" stroke-width="3"><circle cx="10" cy="10" r="8"/><path d="M16 16l8 8"/></svg>
  </div>
</section>

<section class="section testimonials">
  <h2 class="abs">TESTIMONIALS</h2>
  <svg class="abs" style="left:735px;top:2px" width="50" height="42" viewBox="0 0 50 42" fill="var(--orange)"><rect x="30" y="0" width="14" height="14"/><rect x="14" y="14" width="14" height="14"/><rect x="0" y="28" width="12" height="12"/><rect x="36" y="20" width="10" height="10"/></svg>
  <div class="abs avatar" style="left:162px;top:121px" role="img" aria-label="Portrait of a smiling woman"></div>
  <div class="abs t-name" style="left:304px;top:92px">Johan Deo</div>
  <div class="abs t-role" style="left:304px;top:132px">The RightThing</div>
  <p class="abs t-text" style="left:304px;top:194px">Lorem ipsum dolor sit amet, consectetur adipisicing elit, sed do eiusmod tempor incididunt ut labore et dolore magna aliqua. Ut enim ad</p>
  <div class="abs avatar" style="left:623px;top:121px" role="img" aria-label="Portrait of a man in a suit"></div>
  <div class="abs t-name" style="left:765px;top:92px">Johan Deo</div>
  <div class="abs t-role" style="left:765px;top:132px">The RightThing</div>
  <p class="abs t-text" style="left:765px;top:194px">Lorem ipsum dolor sit amet, consectetur adipisicing elit, sed do eiusmod tempor incididunt ut labore et dolore magna aliqua. Ut enim ad</p>
</section>

<section class="schedule">
  <h2 class="abs" style="left:151px;top:42px">SHEDULE AN EVENT</h2>
  <svg class="abs" style="left:498px;top:10px" width="50" height="44" viewBox="0 0 50 44" fill="#fff"><rect x="30" y="0" width="14" height="14"/><rect x="14" y="14" width="14" height="14"/><rect x="0" y="28" width="12" height="12"/><rect x="36" y="20" width="10" height="10"/></svg>
  <div class="abs cal">
    <span class="head">MON</span><span class="head">TUE</span><span class="head">WED</span><span class="head">THU</span><span class="head">FRI</span><span class="head">SAT</span><span class="head">SUN</span>
    <span>1</span><span>2</span><span>3</span><span>4</span><span>5</span><span>6</span><span>7</span>
    <span>8</span><span>9</span><span>10</span><span>11</span><span>12</span><span>13</span><span>14</span>
    <span>15</span><span class="today">16</span><span>17</span><span>18</span><span>19</span><span>20</span><span>21</span>
    <span>22</span><span>23</span><span>24</span><span>25</span><span>26</span><span>27</span><span>28</span>
    <span>29</span><span>30</span><span>31</span><span>1</span><span>2</span><span>3</span><span>4</span>
  </div>
  <div class="btn" style="left:218px;top:381px;width:211px;height:49px;line-height:49px;background:var(--green)">SHEDULE</div>
</section>

<section class="contact">
  <h2 class="abs" style="left:82px;top:30px">CONTACT US</h2>
  <div class="input" style="top:75px;height:47px">Full Name</div>
  <div class="input" style="top:135px;height:45px">Email</div>
  <div class="input" style="top:193px;height:48px">Subject</div>
  <div class="input" style="top:249px;height:102px">Message</div>
  <div class="btn" style="left:84px;top:372px;width:366px;height:48px;line-height:48px;background:var(--orange)">SUBMIT</div>
</section>

<footer class="section footer">
  <div class="social"><span style="left:477px"></span><span style="left:578px"></span><span style="left:667px"></span></div>
  <div class="abs footer-links">HOME <span>|</span> ABOUT US <span>|</span> MEETINGS <span>|</span> EVENTS <span>|</span> CONTACT</div>
  <div class="abs copy">Copy Rights 2016 Brightpath7crew : All Rights Reserved</div>
</footer>

</body>
</html>
```